Palmcrest Loop Tours Splashpage

This webpage will be a holding page until our website is complete. This page needs to be designed to advertise our tours in Honolulu, Hawaii. So it is important to have prices displayed and have a Hawaiian theme.

1. Warm colors - suggest reds?
2. Hawaiian flower incorporated in design

3. Display prices
Adult - single Journey - $20
Adult - 1 Day - $20 (this needs to be displayed as a special deal/price because full price is $25)
Adult - 2 days - $30

Seniors - (62+) 1 Day + 1 Day Free - $20

Children 5 - 17 yrs - 1 Day - $13
Children 5 - 17 yrs - 2 Days - $15
Under 5 Yrs - Free

There will be an online booking button (text on button should say "Book Online", so please make sure it is clear where they can purchase the tickets.

3. A photo of our branded double decker bus should be incorporate on the page.

4. Our Message "Welcome to Palmcrest Loop Tours. Our Open Top Bus ensures you have an unrivalled view of Honolulu and all that this great city has to offer. We pass all of the city’s main sites, offering fantastic photo opportunities along the way. Our tour takes around 90 minutes. You can get on and off the bus as often as you want. Your ticket is valid for one or two days. All departures have commentary in English. If it’s raining, we have a sliding roof to keep you dry. Step on-board and let us show you the best of Honolulu."

5. Some tour sites our tour visits are: Harbor's Arcade, Waikiki beach, Moanu Palace, Keowena Palace/King statue, Rodney's statue

Target Market(s)

We are catering to an international adult audience (ranging from 25 - 60 yrs of age) that handles vacation planning.

Please visit www.brindlecoachways.ee to get an idea of our style.

Requirements
Must have
• 1. prices displayed where they be viewed easily - There will be an online booking button so please make sure it is clear where they can purchase the tickets.

2. Adult - 1 Day - $20 (this needs to be displayed as a special deal/price because full price is $25)

3. Photo of our double decker bus

4. Hawaiian flower incorporated in design

5. Bright colors (make sure orange isn't the main background color) but not overwhelming

6. Logo on webpage
Nice to have
• 1. Images of our tour sites
2. Other Hawaiian images such as palm trees, Maile Lei, Sun with sunglasses, flower lei, parrot, Hawaiian sunsets
Should not have
• -Do not want any shade of orange as the main background color

```html
<!DOCTYPE html>
<html lang="en">
<head>
<meta charset="utf-8">
<title>Palmcrest Loop Tours</title>
<link href="https://fonts.googleapis.com/css2?family=Molengo&family=Bangers&family=Quicksand:wght@500;700&display=swap" rel="stylesheet">
<style>
:root{
  --sky-top:#7fb6e6;
  --sky-low:#dcebf5;
  --sand:#e9e1d2;
  --sand-deep:#d8ccb6;
  --panel:#ffffff;
  --ink:#1d1d1d;
  --maroon:#5b2b2e;
  --red:#e8160e;
  --badge:#d2100c;
  --box-fill:#fff1b9;
  --box-line:#e3d39a;
  --orange:#ff9b1e;
  --tick:#f26a21;
  --dash:#cfcfcf;
}
*{margin:0;padding:0;box-sizing:border-box}
html,body{width:1200px;height:1029px;overflow:hidden}
body{
  position:relative;
  font-family:"Molengo",sans-serif;
  color:var(--ink);
  background:linear-gradient(180deg,var(--sky-top) 0%,var(--sky-low) 30%,#eef2f2 52%,var(--sand) 72%,var(--sand-deep) 100%);
}
.page{
  position:absolute;left:140px;top:0;width:920px;height:913px;
  background:var(--panel);
  border-bottom:2px dashed var(--dash);
}
.brand{
  position:absolute;left:183px;top:30px;
  font-family:"Quicksand",sans-serif;font-weight:700;font-size:44px;
  color:#e8b400;letter-spacing:1px;
}
.gallery{position:absolute;left:0;top:0}
.snap{
  position:absolute;border:6px solid #fff;
  box-shadow:0 2px 6px rgba(0,0,0,.35);
}
.snap.a{left:224px;top:150px;width:180px;height:135px;transform:rotate(-4deg);background:linear-gradient(160deg,#cfd8e6,#a79a8c)}
.snap.b{left:324px;top:125px;width:180px;height:128px;transform:rotate(4deg);background:linear-gradient(160deg,#8d8a5a,#6b4c33)}
.snap.c{left:414px;top:258px;width:170px;height:65px;transform:rotate(-3deg);background:linear-gradient(160deg,#d7b8a8,#9c8873)}
.snap.d{left:465px;top:148px;width:175px;height:130px;transform:rotate(-4deg);background:linear-gradient(160deg,#8ea25d,#6a6a4c)}
.snap.e{left:596px;top:168px;width:172px;height:120px;transform:rotate(-2deg);background:linear-gradient(160deg,#7fa8d8,#cfd0d3)}
.bus{
  position:absolute;left:772px;top:28px;width:200px;height:243px;
  border-radius:16px 16px 6px 6px;
  background:linear-gradient(180deg,#d11d13 0%,#c51a12 60%,#f1c400 85%,#2f2f2f 100%);
}
.badge-string{position:absolute;left:1000px;top:0}
.book-badge{
  position:absolute;left:914px;top:76px;width:206px;height:206px;border-radius:50%;
  background:radial-gradient(circle at 40% 35%,#f03a2c,var(--badge) 65%,#a50b08);
  border:4px solid #fff;box-shadow:0 3px 8px rgba(0,0,0,.35);
  color:#fff;text-align:center;text-decoration:none;
  font-family:"Quicksand",sans-serif;
}
.book-badge::before{
  content:"";position:absolute;inset:7px;border-radius:50%;border:2px dotted rgba(255,255,255,.85);
}
.book-badge .hole{position:absolute;left:95px;top:8px;width:16px;height:16px;border-radius:50%;background:#fff;border:2px solid #999}
.book-badge .lead{position:absolute;left:0;right:0;top:33px;font-size:18px;line-height:18px;font-weight:500}
.book-badge .cta{position:absolute;left:0;right:0;top:68px;font-size:37px;line-height:33px;font-weight:700}
.prices{position:absolute;left:0;top:0}
.price-card{
  position:absolute;top:390px;width:260px;height:158px;
  border:3px solid var(--box-line);border-radius:16px;
  background:var(--box-fill);
  box-shadow:inset 0 0 14px 6px #fff;
  text-align:center;font-size:20px;
}
.price-card.adults{left:170px}
.price-card.seniors{left:470px}
.price-card.children{left:770px}
.price-card h2{
  position:absolute;left:50%;top:-18px;transform:translateX(-50%);
  background:var(--panel);padding:0 14px;
  font-family:"Bangers",sans-serif;font-weight:400;font-size:32px;line-height:34px;
  color:var(--orange);letter-spacing:1px;
  -webkit-text-stroke:1.2px #3a2200;
}
.price-card ul{list-style:none;padding-top:32px;position:relative;z-index:2}
.price-card li{height:35px;line-height:28px}
.price-card .amt{color:var(--red)}
.price-card li.deal{
  margin:0 12px 2px;height:33px;line-height:29px;background:#fff;border:2px solid var(--box-line);border-radius:8px;
  color:var(--red);position:relative;
}
.price-card li.deal svg{position:absolute;left:14px;top:4px}
.flower{position:absolute;border-radius:50%;box-shadow:0 0 0 3px #fff}
.flower.yellow{left:378px;top:494px;width:64px;height:64px;background:radial-gradient(circle,#d7442a 10%,#f4c21b 45%,#f8d94a)}
.flower.pink{left:990px;top:496px;width:66px;height:58px;background:radial-gradient(circle,#b2125a 10%,#ea3a7f 50%,#f0679c)}
.parrot{position:absolute;left:630px;top:498px;width:108px;height:64px;border-radius:50% 40% 20% 60%;background:linear-gradient(120deg,#3b6fd0,#f0c000 50%,#d92f20)}
.intro{position:absolute;left:170px;top:600px;width:862px}
.intro h1{font-size:31px;font-weight:400;color:var(--maroon);line-height:42px}
.intro p{margin-top:14px;font-size:15.2px;line-height:19.6px;color:#2a2a2a}
.intro h3{margin-top:28px;font-size:19.5px;font-weight:400;color:var(--maroon)}
.sites{position:absolute;left:180px;top:797px;width:400px;list-style:none;font-size:14.5px}
.sites li{position:absolute;white-space:nowrap;padding-left:30px;line-height:22px}
.sites li svg{position:absolute;left:0;top:0}
footer{position:absolute;left:0;width:1200px;top:932px;text-align:center;color:#333}
footer .contact{font-family:"Quicksand",sans-serif;font-weight:700;font-size:11.5px}
footer .credit{font-size:10px;color:#555;line-height:12px}
</style>
</head>
<body>
<svg width="0" height="0" style="position:absolute">
  <defs>
    <symbol id="tick" viewBox="0 0 22 20">
      <rect x="1" y="3" width="16" height="15" fill="none" stroke="#f26a21" stroke-width="2.5"/>
      <path d="M4 10 L9 15 L21 1" fill="none" stroke="#f26a21" stroke-width="3.2" stroke-linecap="round" stroke-linejoin="round"/>
    </symbol>
  </defs>
</svg>

<main class="page"></main>

<svg class="route" width="1200" height="340" style="position:absolute;left:0;top:0" aria-hidden="true">
  <path d="M360 0 C340 60 250 40 190 110 C130 180 160 290 240 300 C320 310 400 300 420 300 M555 130 C540 60 480 40 400 60 C330 80 260 90 220 110 M600 320 C650 330 700 310 680 280 M610 140 C640 100 720 110 725 160" fill="none" stroke="#cfcfcf" stroke-width="3" stroke-dasharray="14 9"/>
</svg>

<div class="brand">Palmcrest Loop Tours</div>

<div class="gallery">
  <div class="snap a" role="img" aria-label="Photo of a white colonial palace"></div>
  <div class="snap c" role="img" aria-label="Photo of a city street"></div>
  <div class="snap b" role="img" aria-label="Photo of a bronze statue with flower leis"></div>
  <div class="snap d" role="img" aria-label="Photo of a garden with stone monument"></div>
  <div class="snap e" role="img" aria-label="Photo of a historic palace facade"></div>
</div>

<div class="bus" role="img" aria-label="Photo of the branded red double decker tour bus"></div>

<svg class="badge-string" width="100" height="100" aria-hidden="true">
  <path d="M15 90 C40 40 95 60 60 0" fill="none" stroke="#222" stroke-width="2"/>
</svg>
<a class="book-badge" href="#book">
  <span class="hole"></span>
  <span class="lead">Best prices are<br>online –</span>
  <span class="cta">BOOK<br>ONLINE<br>TODAY</span>
</a>

<section class="prices">
  <div class="price-card adults">
    <h2>Adults</h2>
    <ul>
      <li>Single Journey - <span class="amt">$20</span></li>
      <li class="deal"><svg width="22" height="22" viewBox="0 0 24 24"><path d="M12 1.5l3.1 7 7.4.6-5.6 4.9 1.7 7.3L12 17.4 5.4 21.3l1.7-7.3L1.5 9.1l7.4-.6z" fill="#e8160e" stroke="#111" stroke-width="1.5"/></svg>1 Day - $20</li>
      <li>2 days - <span class="amt">$30</span></li>
    </ul>
  </div>
  <div class="price-card seniors">
    <h2>Seniors</h2>
    <ul>
      <li>(62+) 1 Day +</li>
      <li>1 Day Free - <span class="amt">$20</span></li>
    </ul>
  </div>
  <div class="price-card children">
    <h2>Children</h2>
    <ul>
      <li>5 - 17 yrs - 1 Day - <span class="amt">$13</span></li>
      <li>5 - 17 yrs - 2 Days - <span class="amt">$15</span></li>
      <li>Under 5 Yrs - <span class="amt">Free</span></li>
    </ul>
  </div>
  <div class="flower yellow" role="img" aria-label="Yellow hibiscus flower"></div>
  <div class="parrot" role="img" aria-label="Colourful parrot perched on the box"></div>
  <div class="flower pink" role="img" aria-label="Pink hibiscus flower"></div>
</section>

<section class="intro">
  <h1>Welcome to Palmcrest Loop Tours</h1>
  <p>Our Open Top Bus ensures you have an unrivalled view of Honolulu and all that this great city has to offer. We pass all of the city’s main sites, offering fantastic photo opportunities along the way. Our tour takes around 90 minutes. You can get on and off the bus as often as you want. Your ticket is valid for one or two days. All departures have commentary in English. If it’s raining, we have a sliding roof to keep you dry. Step on-board and let us show you the best of Honolulu.</p>
  <h3>Some tour sites our tour visits are:</h3>
</section>

<ul class="sites">
  <li style="left:0;top:0;color:#444"><svg width="22" height="20"><use href="#tick"/></svg>Harbor's Arcade</li>
  <li style="left:0;top:28px;color:#444"><svg width="22" height="20"><use href="#tick"/></svg>Waikiki beach</li>
  <li style="left:0;top:56px;color:#444"><svg width="22" height="20"><use href="#tick"/></svg>Moanu Palace</li>
  <li style="left:171px;top:0"><svg width="22" height="20"><use href="#tick"/></svg>Keowena Palace/King statue</li>
  <li style="left:171px;top:28px"><svg width="22" height="20"><use href="#tick"/></svg>Rodney's statue</li>
</ul>

<footer>
  <div class="contact">Palmcrest Loop Tours - Address Here: Honolulu, Hawaii - Tel. (123) 456 789</div>
  <div class="credit">Site &amp; Online Booking by Tixwave.com</div>
</footer>
</body>
</html>
```